need eczema bath soak label/bag

need you to recreate this please. ai file. recreate this exact image please. ...if you want a big tip, create some different styles.

Colors
0054AA
0677BA
7BADD7
CADEEF
E8F1F8

```html
<!DOCTYPE html>
<html lang="en">
<head>
<meta charset="utf-8">
<title>Ocean Bath Soak Label</title>
<link rel="stylesheet" href="https://fonts.googleapis.com/css2?family=Poppins:wght@500;600;700;800&display=swap">
<style>
  :root {
    --ink: #0d2e2a;
    --paper: #ffffff;
    --frame: #2a2a2a;
    --sea-light: #a9dcc9;
    --sea: #4fb597;
    --sea-deep: #3e9f86;
    --shallows: #c7b98c;
    --foam: #f1eee8;
    --sand: #d6ae79;
    --sand-deep: #cfa571;
  }
  html, body {
    margin: 0;
    padding: 0;
    width: 1200px;
    height: 2771px;
    overflow: hidden;
    background: var(--paper);
  }
  body {
    position: relative;
    font-family: "Poppins", sans-serif;
    color: var(--ink);
  }
  .label {
    position: absolute;
    left: 177px;
    width: 846px;
    height: 1095px;
    overflow: hidden;
    background: var(--paper);
  }
  .label--flat {
    top: 252px;
    outline: 1px solid var(--frame);
  }
  .label--pouch {
    top: 1640px;
    transform: scale(0.95);
    transform-origin: top center;
  }
  .shore-photo {
    position: absolute;
    left: 0;
    top: 200px;
    width: 100%;
    height: 895px;
    background: linear-gradient(to bottom,
      rgba(255,255,255,0) 0%,
      var(--sea-light) 6%,
      var(--sea) 15%,
      var(--sea-deep) 20%,
      var(--shallows) 30%,
      var(--foam) 44%,
      var(--foam) 54%,
      var(--sand) 64%,
      var(--sand-deep) 100%);
  }
  .line {
    position: absolute;
    left: 0;
    width: 100%;
    margin: 0;
    text-align: center;
    line-height: 1;
    white-space: nowrap;
  }
  .kicker { top: 230px; font-size: 32px; font-weight: 700; letter-spacing: 5px; }
  .headline { font-size: 70px; font-weight: 800; letter-spacing: 1px; }
  .headline--1 { top: 277px; }
  .headline--2 { top: 360px; }
  .headline--3 { top: 445px; }
  .blurb {
    top: 538px;
    font-size: 9px;
    font-weight: 700;
    line-height: 17px;
  }
  .product { top: 604px; font-size: 21px; font-weight: 600; letter-spacing: 1px; }
  .batch {
    position: absolute;
    top: 630px;
    left: 323px;
    width: 200px;
    height: 60px;
  }
  .batch text { font-family: "Poppins", sans-serif; font-size: 24px; font-weight: 600; letter-spacing: 3px; fill: var(--ink); }
  .category { top: 699px; font-size: 17px; font-weight: 700; letter-spacing: 3px; }
  .brand-mark {
    position: absolute;
    top: 806px;
    left: 393px;
    width: 60px;
    height: 60px;
    background: var(--ink);
  }
  .brand-name { top: 914px; font-size: 22px; font-weight: 600; letter-spacing: 5px; }
  .lot-number { top: 986px; font-size: 17px; font-weight: 500; letter-spacing: 6px; }
</style>
</head>
<body>

<section class="label label--flat">
  <div class="shore-photo" role="img" aria-label="Aerial photo of turquoise sea waves breaking into white foam over golden sand"></div>
  <p class="line kicker">THE</p>
  <p class="line headline headline--1">OCEAN</p>
  <p class="line headline headline--2">HEALED</p>
  <p class="line headline headline--3">MY A BAG</p>
  <p class="line blurb">LOREM IPSUM DOLOR SIT AMET, CONSECTETUER<br>ADIPISCING ELIT, SED DIAM NONUMMY NIBH<br>EUISMOD TINCIDUNT UT LAOREET DOLORE MAGNA</p>
  <p class="line product">OCEAN IN A BAG</p>
  <svg class="batch" viewBox="0 0 200 60" aria-label="B77 6A119">
    <defs><path id="batch-arc-a" d="M10,12 Q100,72 190,12"/></defs>
    <text text-anchor="middle"><textPath href="#batch-arc-a" startOffset="50%">B77 6A119</textPath></text>
  </svg>
  <p class="line category">BATH SOAK</p>
  <div class="brand-mark"></div>
  <p class="line brand-name">TIDEWELL</p>
  <p class="line lot-number">123456789</p>
</section>

<section class="label label--pouch">
  <div class="shore-photo" role="img" aria-label="Aerial photo of turquoise sea waves breaking into white foam over golden sand"></div>
  <p class="line kicker">THE</p>
  <p class="line headline headline--1">OCEAN</p>
  <p class="line headline headline--2">HEALED</p>
  <p class="line headline headline--3">MY A BAG</p>
  <p class="line blurb">LOREM IPSUM DOLOR SIT AMET, CONSECTETUER<br>ADIPISCING ELIT, SED DIAM NONUMMY NIBH<br>EUISMOD TINCIDUNT UT LAOREET DOLORE MAGNA</p>
  <p class="line product">OCEAN IN A BAG</p>
  <svg class="batch" viewBox="0 0 200 60" aria-label="B77 6A119">
    <defs><path id="batch-arc-b" d="M10,12 Q100,72 190,12"/></defs>
    <text text-anchor="middle"><textPath href="#batch-arc-b" startOffset="50%">B77 6A119</textPath></text>
  </svg>
  <p class="line category">BATH SOAK</p>
  <div class="brand-mark"></div>
  <p class="line brand-name">TIDEWELL</p>
  <p class="line lot-number">123456789</p>
</section>

</body>
</html>
```